IT Services and Hardware Tri-Fold Brochure

We need a brochure design for a new IT company based in Melbourne, Australia called Tindlefar. We provide multiple IT services such as IT system setup, network management, domain / web hosting / emails, and ongoing IT support services. We are still working on our website, but have attached a sample of what our landing page will look like to help with colouring. We've also attached a draft of the content we will have.

The size we are printing the brochure is A4 which will be folded into equal thirds and double sided (tri-fold).

Industry/Entity Type

Information Technology

Font styles to use
Serif
Sans Serif

Requirements
Must have
• We are trying to go with a flat design sort of feel. You don't need to have the full details from the files attached, if it looks to crowded, we can shorten the information.

```html
<!DOCTYPE html>
<html lang="en">
<head>
<meta charset="utf-8">
<title>Tindlefar – IT Services Tri-Fold Brochure</title>
<link href="https://fonts.googleapis.com/css2?family=Open+Sans:wght@400;600;700;800&display=swap" rel="stylesheet">
<style>
  :root {
    --blue: #1a72b9;
    --yellow: #f4c431;
    --charcoal: #3b3e43;
    --ink: #2a2c30;
    --paper: #ffffff;
    --backdrop: #e8e6e2;
    --muted: #6b6f75;
  }
  * { box-sizing: border-box; margin: 0; padding: 0; }
  html, body { width: 1200px; height: 900px; overflow: hidden; }
  body {
    background: var(--backdrop);
    font-family: "Open Sans", Arial, sans-serif;
    color: var(--ink);
    position: relative;
  }
  .sheet {
    position: absolute;
    left: 290px;
    width: 620px;
    height: 438px;
    display: grid;
    grid-template-columns: repeat(3, 1fr);
    background: var(--paper);
    box-shadow: 0 2px 8px rgba(0,0,0,.15);
  }
  .sheet--outside { top: 8px; }
  .sheet--inside { top: 454px; }
  .panel {
    position: relative;
    overflow: hidden;
    border-right: 1px solid #e3e3e3;
    display: flex;
    flex-direction: column;
  }
  .panel:last-child { border-right: none; }

  .tab {
    display: inline-block;
    background: var(--yellow);
    color: var(--ink);
    font-weight: 700;
    font-size: 10.5px;
    padding: 3px 10px 3px 8px;
    line-height: 1.15;
  }
  .tab--dark { background: var(--charcoal); color: #fff; }
  .body-copy { font-size: 6.2px; line-height: 1.45; }
  .body-copy + .body-copy { margin-top: 3px; }
  .ticks { list-style: none; font-size: 6.4px; line-height: 1.55; }
  .ticks li { position: relative; padding-left: 11px; }
  .ticks li::before { content: "✓"; position: absolute; left: 1px; font-weight: 700; }

  /* Outside – support panel */
  .support-block { background: var(--blue); color: #fff; padding: 12px 10px 12px; }
  .support-block .tab { margin: -6px 0 8px -10px; }
  .support-block .body-copy { font-size: 6.6px; }
  .support-block .ticks { margin-top: 6px; font-size: 6.8px; }
  .pbx-pitch {
    font-weight: 700; font-size: 8.6px; line-height: 1.35;
    text-align: center; padding: 12px 10px 8px;
  }
  .pbx-list { padding: 0 10px; font-size: 6.8px; }

  /* Outside – middle panel */
  .promo-frame { background: var(--charcoal); padding: 10px 10px 12px; }
  .promo-photo { position: relative; height: 248px; background: linear-gradient(160deg, #f2f2f2 0%, #cfd6de 55%, #9aa6b3 100%); }
  .promo-callout {
    position: absolute; left: 12px; right: 10px; top: 60px;
    background: var(--yellow); color: var(--ink);
    font-weight: 800; font-size: 7.6px; line-height: 1.3;
    text-align: center; padding: 8px 6px; text-transform: uppercase;
  }
  .brand-small { display: flex; align-items: center; justify-content: center; gap: 4px; font-size: 8px; font-weight: 600; color: var(--muted); padding: 10px 0 8px; }
  .brand-small .mark { width: 8px; height: 8px; border-radius: 50%; border: 1px solid var(--muted); }
  .phone-band { background: var(--blue); color: #fff; font-weight: 700; font-size: 11px; display: flex; align-items: center; justify-content: center; gap: 5px; height: 24px; }
  .rule-band { background: var(--charcoal); height: 12px; margin-top: 6px; }
  .web-line { display: flex; align-items: center; justify-content: center; gap: 5px; font-weight: 700; font-size: 10px; padding: 10px 0; }

  /* Outside – cover */
  .cover-brand { display: flex; align-items: center; gap: 6px; height: 58px; padding-left: 22px; font-size: 17px; font-weight: 600; color: var(--muted); }
  .cover-brand .mark { width: 18px; height: 18px; border-radius: 50%; border: 2px solid var(--muted); }
  .cover-photo { height: 168px; background: linear-gradient(150deg, #eef1f4 0%, #b7c3cf 45%, #5d6d7e 100%); }
  .cover-lower { flex: 1; background: var(--yellow); padding: 12px 14px; display: flex; flex-direction: column; }
  .cover-title { background: #fff; font-weight: 700; font-size: 8.4px; line-height: 1.3; text-align: center; padding: 10px 6px; text-transform: uppercase; }
  .cover-tagline { font-size: 6.6px; font-weight: 700; text-align: center; margin-top: 12px; padding-bottom: 2px; border-bottom: 1px solid var(--ink); }
  .cover-phone { margin-top: auto; align-self: flex-end; background: var(--charcoal); color: #fff; font-weight: 700; font-size: 10px; padding: 6px 10px; display: flex; align-items: center; gap: 5px; }

  /* Inside – setup */
  .setup-head { padding: 10px 0 6px; }
  .setup-photo { height: 88px; margin: 0 10px; background: linear-gradient(135deg, #dbe6f0, #5f86ad 60%, #24466a); }
  .setup-block { background: var(--blue); color: #fff; padding: 8px 10px; margin-top: 8px; font-size: 6.4px; line-height: 1.4; }
  .setup-block strong { font-size: 7px; display: block; }
  .setup-block p + strong { margin-top: 5px; }
  .setup-list { padding: 10px 10px 8px; }
  .setup-list h3 { font-size: 7px; font-weight: 600; margin-bottom: 4px; }
  .setup-list .ticks { font-size: 6.8px; }
  .setup-photo-2 { flex: 1; margin: 0 10px; min-height: 60px; background: linear-gradient(150deg, #cfd9e3, #8ea3b8 50%, #3d4e62); }
  .accent-foot { height: 11px; background: var(--yellow); margin-top: 6px; flex: none; }

  /* Inside – network */
  .network-top { background: var(--charcoal); padding-top: 8px; }
  .network-top .tab { margin-left: 10px; }
  .network-copy { background: var(--blue); color: #fff; padding: 8px 10px; }
  .network-photo { height: 100px; margin: 8px 14px; background: linear-gradient(180deg, #f4f6f9, #b9c7d6 55%, #6d86a3); }
  .range-band { background: var(--blue); color: #fff; font-weight: 700; font-size: 7px; padding: 3px 10px; margin: 0 10px; }
  .network-list { padding: 8px 14px 0; }
  .network-list h3 { font-size: 7px; font-weight: 700; margin-bottom: 3px; }
  .network-list .ticks { font-size: 6.6px; }

  /* Inside – consulting */
  .consult-block { background: var(--blue); color: #fff; padding: 0 10px 10px; }
  .consult-block .tab { margin: 8px 0 6px -10px; }
  .consult-block .body-copy { font-size: 6.4px; }
  .consult-note { font-weight: 700; font-size: 6.8px; text-align: center; margin-top: 6px; }
  .domain { padding: 10px 10px 0; flex: 1; }
  .domain .tab { margin-left: -10px; font-size: 10px; margin-bottom: 10px; }
  .domain .body-copy { font-size: 6.8px; }
  .domain .body-copy + .body-copy { margin-top: 8px; }
</style>
</head>
<body>

<section class="sheet sheet--outside">
  <article class="panel panel--support">
    <div class="support-block">
      <h2 class="tab">IT Support Solutions</h2>
      <p class="body-copy">Tindlefar has the people and the technology to ensure that your core infrastructure systems are kept running day to day. We deliver ongoing support so your staff can focus on their work, not on their computers.</p>
      <p class="body-copy">Our IT Support team understands how crucial it is to resolve issues as quickly as possible, minimising any impact on trading and productivity. The following support services are available from us:</p>
      <ul class="ticks">
        <li>On-site Support</li>
        <li>Offsite Support (Remote Assistance)</li>
        <li>Contract / Term Based Support</li>
        <li>Technical Loan Staff (IT Support Sourcing)</li>
      </ul>
    </div>
    <p class="pbx-pitch">Make a transition from your local number (03) to 1300 or 1800 number and make it future proof, use Tindlefar's hosted PBX system. It's easier and cheaper than you think. A turnkey solution for modern business telephony that you've been searching for...</p>
    <ul class="ticks pbx-list">
      <li>Cloud Hosted (No purchasing, maintenance and upgrades to worry about)</li>
      <li>Call Quality Guaranteed</li>
      <li>Multi-site Capable (Free Inter-office calls)</li>
      <li>Feature Rich and At the Forefront of Technology</li>
      <li>All the features that you'll need, without the cost</li>
    </ul>
  </article>

  <article class="panel panel--promo">
    <div class="promo-frame">
      <div class="promo-photo" role="img" aria-label="Photo of a smiling office worker at a desk with a colleague behind">
        <p class="promo-callout">You have a business to run. Profits to increase. Employees to motivate. Investors to impress. You don't have time for a phone system that doesn't work.</p>
      </div>
    </div>
    <div class="brand-small"><span class="mark"></span>Tindlefar</div>
    <div class="phone-band">
      <svg width="10" height="10" viewBox="0 0 10 10" aria-hidden="true"><circle cx="5" cy="5" r="4.4" fill="none" stroke="#fff" stroke-width="1"/><path d="M3.4 2.8c.3-.3.6-.2.8.1l.4.7c.1.2 0 .4-.2.6l-.3.3c.3.6.8 1.1 1.4 1.4l.3-.3c.2-.2.4-.3.6-.2l.7.4c.3.2.4.5.1.8-.5.6-1.2.6-2 .1-.9-.6-1.600-1.3-2-2.2-.3-.7-.2-1.3.2-1.700z" fill="#fff"/></svg>
      1300555014
    </div>
    <div class="rule-band"></div>
    <div class="web-line">
      <svg width="10" height="10" viewBox="0 0 10 10" aria-hidden="true"><circle cx="5" cy="5" r="4.3" fill="none" stroke="#2a2c30" stroke-width="1"/><ellipse cx="5" cy="5" rx="1.8" ry="4.3" fill="none" stroke="#2a2c30" stroke-width=".8"/><path d="M.8 5h8.4M1.6 2.8h6.8M1.6 7.2h6.8" stroke="#2a2c30" stroke-width=".7"/></svg>
      www.yourwebsite.com
    </div>
  </article>

  <article class="panel panel--cover">
    <div class="cover-brand"><span class="mark"></span>Tindlefar</div>
    <div class="cover-photo" role="img" aria-label="Photo of a hand touching a glowing digital network interface"></div>
    <div class="cover-lower">
      <h1 class="cover-title">Information &amp;<br>Communication<br>Technology</h1>
      <p class="cover-tagline">Helping you with evolving technology needs</p>
      <div class="cover-phone">
        <svg width="10" height="10" viewBox="0 0 10 10" aria-hidden="true"><circle cx="5" cy="5" r="4.4" fill="none" stroke="#fff" stroke-width="1"/><path d="M3.4 2.8c.3-.3.6-.2.8.1l.4.7c.1.2 0 .4-.2.6l-.3.3c.3.6.8 1.1 1.4 1.4l.3-.3c.2-.2.4-.3.6-.2l.7.4c.3.2.4.5.1.8-.5.6-1.2.6-2 .1-.9-.6-1.6-1.3-2-2.2-.3-.7-.2-1.3.2-1.7z" fill="#fff"/></svg>
        1300555014
      </div>
    </div>
  </article>
</section>

<section class="sheet sheet--inside">
  <article class="panel panel--setup">
    <div class="setup-head"><h2 class="tab">IT Systems Setup</h2></div>
    <div class="setup-photo" role="img" aria-label="Photo of a man facing a wall of floating digital screens"></div>
    <div class="setup-block">
      <strong>Phone System:</strong>
      <p>PBX, Unifies (Inbound/Outbound, Progressive, Predictive)</p>
      <strong>Servers Setup:</strong>
      <p>Various business oriented server installation and configuration</p>
    </div>
    <div class="setup-list">
      <h3>Desktop and Server Technology:</h3>
      <ul class="ticks">
        <li>Directory services deployment and upgrade</li>
        <li>Enterprise mail server deployment and migration</li>
        <li>Web Server, File Server, DNS and DHCP</li>
        <li>Open source server administration</li>
        <li>Router, Firewall, FTP, Web, DNS/DHCP, Proxy, Mail, Storage</li>
        <li>Misc: CRM and ticketing system</li>
      </ul>
    </div>
    <div class="setup-photo-2" role="img" aria-label="Photo of a businessman sketching a cloud connected to devices"></div>
    <div class="accent-foot"></div>
  </article>

  <article class="panel panel--network">
    <div class="network-top"><h2 class="tab tab--dark">Network Management</h2></div>
    <div class="network-copy">
      <p class="body-copy">Networks are the backbone of your business. We design, build and maintain secure, reliable networks that connect your people, offices and cloud services. We provide network assessment, design, deployment and ongoing support.</p>
    </div>
    <div class="network-photo" role="img" aria-label="Photo of a bright server room with rows of racks"></div>
    <p class="range-band">The range of network solutions includes:</p>
    <div class="network-list">
      <h3>Application Delivery Management</h3>
      <ul class="ticks">
        <li>Traffic Management</li>
        <li>Load Balancing</li>
        <li>Internet Protocol (IP) telephony/Voice Over IP (VoIP)</li>
        <li>Network Management/Monitoring</li>
        <li>Switching &amp; Routing</li>
        <li>Virtual Private Network (VPN)/Security</li>
        <li>Wide Area Network (WAN)</li>
        <li>WAN caching / compression solutions</li>
        <li>Wireless Networking</li>
        <li>Network security</li>
      </ul>
    </div>
  </article>

  <article class="panel panel--consulting">
    <div class="consult-block">
      <h2 class="tab">IT Transformation Consulting</h2>
      <p class="body-copy">In this fast growing and ever changing IT world it can be difficult to choose and implement the latest and emerging technologies. Tindlefar consultants work alongside your team to review your current systems, plan a clear roadmap and deliver change with minimal disruption. We help you select the right platforms, migrate safely to the cloud and get real value from every technology investment you make.</p>
      <p class="consult-note">We do now offer Open Source Software consultancy.</p>
    </div>
    <div class="domain">
      <h2 class="tab">Domain Registration,<br>Hosting - Web and Email</h2>
      <p class="body-copy">Still using a free webmail address or email provided by your ISP? Start with your own domain and host your email with Tindlefar.</p>
      <p class="body-copy">Register your own domain and show your presence to the world around you. Domain name shows your behaviour, who you are. Search the domain that best represents you and your business.</p>
      <p class="body-copy">We understand your website is your online presence and also your shop window and one of your greatest assets. Tindlefar offers great value, feature rich, secure and reliable hosting services.</p>
      <p class="body-copy">We provide affordable secure cloud hosting solutions (open source and commercial platforms).</p>
    </div>
    <div class="accent-foot"></div>
  </article>
</section>

</body>
</html>
```